Exercise Physiologist needs a Brochure

I am Exercise Physiologist providing exercise therapy for a variety of conditions. I have a logo and recent business card design. I like the black background like the front of the business cards. I have attached the flyer information required. I have also attached a few photos however they do not have to be used, happy to have no photos at all.

Industry/Entity Type

Health And Wellness

Font styles to use
Sans Serif

Requirements
Must have
• Please also add instagram @morvalecare
Nice to have
• tri-fold brochure

```html
<!DOCTYPE html>
<html lang="en">
<head>
<meta charset="utf-8">
<title>Morvale Care – Tri-fold Brochure</title>
<link href="https://fonts.googleapis.com/css2?family=Open+Sans:ital,wght@0,300;0,400;0,600;1,400&display=swap" rel="stylesheet">
<style>
:root{
  --page:#d6d7d9;
  --ink:#161616;
  --ink-soft:#2e2f31;
  --blue:#5aa7dc;
  --blue-deep:#2f74b5;
  --white:#ffffff;
  --text-dark:#4a4a4a;
  --text-light:#f1f1f1;
  --rule:#8dbfe6;
}
*{margin:0;padding:0;box-sizing:border-box}
html,body{width:849px;height:1200px;overflow:hidden;background:var(--page)}
body{font-family:"Open Sans",Arial,sans-serif;position:relative}
.spread{position:absolute;left:63px;width:735px;height:520px;box-shadow:0 6px 10px rgba(0,0,0,.25);overflow:hidden}
.spread--outside{top:55px}
.spread--inside{top:624px}
.spread__bg{position:absolute;inset:0}
.panel{position:absolute;top:0;width:245px;height:520px}
.panel--left{left:0}.panel--mid{left:245px}.panel--right{left:490px}
.fold{position:absolute;top:0;width:1px;height:520px;background:rgba(255,255,255,.12)}
.headline{position:absolute;left:21px;font-weight:300;font-size:24px;line-height:32px;color:var(--blue);letter-spacing:.5px}
.tagline{position:absolute;left:21px;width:210px;font-style:italic;font-size:10.5px;line-height:13px;font-weight:400}
.body-copy{position:absolute;font-size:10px;line-height:13px;text-align:justify;font-weight:400}
.rule{position:absolute;height:1px;background:var(--rule)}
.dark{color:var(--text-light)}
.muted{color:var(--text-dark)}
.subhead{position:absolute;font-size:13.5px;color:var(--blue);line-height:19px;font-weight:400}
.name{position:absolute;width:245px;text-align:center;font-weight:300;font-size:29px;color:var(--blue);line-height:34px;white-space:nowrap}
.role{position:absolute;width:245px;text-align:center;font-weight:300;font-size:16px;line-height:20px;white-space:nowrap}
.address{position:absolute;top:256px;width:245px;text-align:center;font-size:11px;line-height:18px;color:var(--white)}
.brand{position:absolute;display:flex;align-items:center;gap:7px;color:var(--blue);font-weight:400;white-space:nowrap}
.brand__dot{border-radius:50%;background:var(--blue);flex:none}
.social{position:absolute;top:482px;left:0;width:245px;display:flex;justify-content:center;gap:10px;font-size:8px;color:#d8d8d8}
.social span{display:flex;align-items:center;gap:4px}
.social i{width:14px;height:14px;border-radius:50%;border:1px solid #cfcfcf;display:inline-block}
.credentials{position:absolute;top:474px;width:245px;text-align:center;font-size:7.6px;line-height:11.5px;color:#e0e0e0}
.cta{position:absolute;left:21px;top:448px;font-size:13px;line-height:17px;color:var(--white)}
.phone{position:absolute;left:21px;top:488px;display:flex;align-items:center;gap:9px;font-size:13.5px;color:var(--blue)}
.conditions{position:absolute;left:20px;top:266px;width:220px;list-style:none;font-size:10.5px;line-height:14.5px;color:var(--white)}
.conditions li{position:relative;padding-left:17px}
.conditions li::before{content:"›";position:absolute;left:0;top:2px;width:9px;height:9px;border:1px solid #cfcfcf;border-radius:50%;font-size:9px;line-height:7px;text-align:center;color:#cfcfcf}
</style>
</head>
<body>

<section class="spread spread--outside">
  <svg class="spread__bg" width="735" height="520" viewBox="0 0 735 520">
    <defs>
      <linearGradient id="darkFade" x1="0" y1="0" x2="0" y2="1">
        <stop offset="0" stop-color="#0e0e0e"/><stop offset="1" stop-color="#353638"/>
      </linearGradient>
      <linearGradient id="lightFade" x1="0" y1="0" x2="1" y2="0">
        <stop offset="0" stop-color="#ffffff"/><stop offset="1" stop-color="#e4e5e7"/>
      </linearGradient>
      <linearGradient id="trailPhoto" x1="0" y1="0" x2="0" y2="1">
        <stop offset="0" stop-color="#7c8c3a"/><stop offset=".55" stop-color="#4f5a2c"/><stop offset="1" stop-color="#a89a7e"/>
      </linearGradient>
      <linearGradient id="walkPhoto" x1="0" y1="0" x2="0" y2="1">
        <stop offset="0" stop-color="#c9b49a"/><stop offset="1" stop-color="#5d4c3c"/>
      </linearGradient>
    </defs>
    <rect width="735" height="520" fill="url(#darkFade)"/>
    <rect x="245" y="0" width="245" height="370" fill="#0b0b0b"/>
    <path d="M0 0H245V300C175 322 90 385 0 408Z" fill="url(#lightFade)"/>
    <path d="M245 0H735V78C640 92 520 90 420 56C340 28 290 10 245 10Z" fill="url(#lightFade)"/>
    <path d="M245 14C300 20 350 40 420 66C520 100 640 100 735 86" fill="none" stroke="#77797d" stroke-width="7"/>
    <path d="M490 92C570 100 650 98 735 86V372C640 384 560 380 490 370Z" fill="url(#trailPhoto)" role="img" aria-label="Photo of a woman running along a tree-lined trail"/>
    <path d="M0 420C90 392 180 330 290 352C420 380 560 392 735 376" fill="none" stroke="#9a9ca0" stroke-width="6"/>
    <path d="M0 412C90 384 180 322 290 344C420 372 560 384 735 368" fill="none" stroke="var(--blue)" stroke-width="8"/>
    <circle cx="84" cy="330" r="66" fill="#d7e6f2"/>
    <circle cx="84" cy="330" r="58" fill="url(#walkPhoto)" role="img" aria-label="Close-up photo of walking shoes on a gravel path"/>
    <circle cx="368" cy="88" r="64" fill="#ffffff"/>
    <circle cx="368" cy="88" r="56" fill="var(--blue)"/>
  </svg>
  <div class="fold" style="left:245px"></div><div class="fold" style="left:490px"></div>

  <div class="panel panel--left">
    <h1 class="headline" style="top:28px">HEAL<br>THROUGH<br>MOVEMENT</h1>
    <p class="tagline muted" style="top:127px">Discover how important the correct exercise technique is to your success</p>
    <div class="rule" style="left:21px;top:162px;width:118px"></div>
    <p class="body-copy muted" style="left:21px;top:170px;width:215px">Performing the right exercise the wrong way can do more harm than good. I can teach you what, how and when to perform your tailored exercise program to get the best results.</p>
    <p class="cta">Call or email me today to see<br>how I can help you.</p>
    <div class="phone">
      <svg width="14" height="14" viewBox="0 0 14 14"><circle cx="7" cy="7" r="6.2" fill="none" stroke="var(--blue)" stroke-width="1.2"/><path d="M4.3 4.2l1.4-.4.8 1.6-.8.7c.4.9 1 1.5 1.9 1.9l.7-.8 1.6.8-.4 1.4c-3 .2-5.4-2.2-5.2-5.2z" fill="var(--blue)"/></svg>
      0400 555 218
    </div>
  </div>

  <div class="panel panel--mid">
    <h2 class="name" style="top:182px">Claire Dunmore</h2>
    <p class="role" style="top:215px;color:#e6e6e6">Exercise Physiologist</p>
    <div class="rule" style="left:70px;top:240px;width:105px"></div>
    <p class="address">Unit 4, 18 Harlow Lane NORTH BAYVIEW<br>(Kestrel Fitness)<br>hello@morvalecare.com</p>
    <div class="brand" style="left:44px;top:412px;font-size:23px"><span class="brand__dot" style="width:24px;height:24px"></span>Morvale Care</div>
    <div class="social"><span><i></i>Morvale</span><span><i></i>@morvalecare</span></div>
  </div>

  <div class="panel panel--right">
    <div class="brand" style="left:28px;top:22px;font-size:24px"><span class="brand__dot" style="width:32px;height:32px"></span>Morvale Care</div>
    <h2 class="name" style="top:422px">Claire Dunmore</h2>
    <p class="role" style="top:454px;color:#e6e6e6">Exercise Physiologist</p>
    <p class="credentials" style="top:478px">B.AppSci – Human Mvmt<br>Grad Dip – ExRehab<br>Cert IV – Training &amp; Assessment</p>
  </div>
</section>

<section class="spread spread--inside">
  <svg class="spread__bg" width="735" height="520" viewBox="0 0 735 520">
    <defs>
      <linearGradient id="darkFade2" x1="0" y1="0" x2="0" y2="1">
        <stop offset="0" stop-color="#0e0e0e"/><stop offset="1" stop-color="#2f3032"/>
      </linearGradient>
      <linearGradient id="kneePhoto" x1="0" y1="0" x2="1" y2="1">
        <stop offset="0" stop-color="#d9d9d9"/><stop offset=".45" stop-color="#9b9b9b"/><stop offset="1" stop-color="#3c3c3c"/>
      </linearGradient>
      <linearGradient id="gymPhoto" x1="0" y1="0" x2="1" y2="1">
        <stop offset="0" stop-color="#8fb6d6"/><stop offset=".5" stop-color="#3c5a73"/><stop offset="1" stop-color="#1b2a36"/>
      </linearGradient>
    </defs>
    <rect width="735" height="520" fill="url(#darkFade2)"/>
    <rect x="245" y="0" width="245" height="520" fill="#ffffff"/>
    <path d="M0 338C80 308 170 318 245 358V520H0Z" fill="url(#kneePhoto)" role="img" aria-label="Photo of a knee with the painful area highlighted in red"/>
    <path d="M0 330C80 300 170 310 245 350" fill="none" stroke="#ffffff" stroke-width="4"/>
    <path d="M0 324C80 294 170 304 245 344" fill="none" stroke="var(--blue)" stroke-width="6"/>
    <path d="M490 0H735V128C650 168 560 186 490 186Z" fill="url(#gymPhoto)" role="img" aria-label="Photo of a rack of dumbbells in a gym"/>
    <path d="M490 194C560 194 650 176 735 136" fill="none" stroke="var(--blue)" stroke-width="6"/>
    <circle cx="368" cy="90" r="56" fill="#ffffff" stroke="#e2e2e2" stroke-width="2"/>
    <circle cx="368" cy="90" r="48" fill="var(--blue)"/>
  </svg>
  <div class="fold" style="left:245px;background:rgba(0,0,0,.08)"></div><div class="fold" style="left:490px;background:rgba(0,0,0,.08)"></div>

  <div class="panel panel--left">
    <h1 class="headline" style="top:20px">HEAL<br>THROUGH<br>MOVEMENT</h1>
    <p class="tagline dark" style="top:121px">Don't let the right exercise but the wrong technique hinder your recovery</p>
    <h3 class="subhead" style="left:20px;top:164px">What is an Exercise Physiologist?</h3>
    <div class="rule" style="left:20px;top:188px;width:118px"></div>
    <p class="body-copy dark" style="left:20px;top:196px;width:215px">Exercise Physiologists are university educated health professionals trained to provide exercise therapy for pain and injury, pre and post surgery, mental health and chronic disease. They are registered providers with RoadCover, WorkGuard, HealthLink, Veterans Support Office and many Private Health funds.</p>
  </div>

  <div class="panel panel--mid">
    <h3 class="subhead" style="left:0;width:245px;text-align:center;top:176px">How can I help you?</h3>
    <div class="rule" style="left:72px;top:204px;width:100px"></div>
    <div class="body-copy muted" style="left:21px;top:229px;width:205px">
      <p>I have over 13 years of experience working as an Exercise Physiologist and have been working in the sport and fitness industry since 1996. I understand that everyone's health and exercise experience is unique and will tailor a program to suit you and your lifestyle.</p>
      <p style="margin-top:9px">Managing your condition involves working with you to develop the best exercises and teaching you the correct technique essential to improve. Home and gym based programs can be provided.</p>
      <p style="margin-top:9px">When appropriate I can also work with your current treating health practitioner to provide a holistic approach to your recovery.</p>
    </div>
  </div>

  <div class="panel panel--right">
    <h3 class="subhead" style="left:20px;top:212px;width:220px">Common conditions that benefit from exercise therapy</h3>
    <ul class="conditions">
      <li>Back pain</li>
      <li>Joint pain</li>
      <li>Pain relating to exercise</li>
      <li>Arthritis</li>
      <li>Anxiety relating to exercise</li>
      <li>Depression and Anxiety</li>
      <li>Chronic diseases such as diabetes, heart and lung disease.</li>
      <li>Motor vehicle accidents</li>
    </ul>
    <p class="body-copy dark" style="left:20px;top:431px;width:215px">Performing the right exercise the wrong way can do more harm than good. I can teach you what, how and when to perform your tailored exercise program to get the best results.</p>
  </div>
</section>

</body>
</html>
```